iPad Apps for Energy Industry w/ IT Consulting Business Needs a Brochure Design

We need a brochure and business card design for an IT development and consulting company based in Westlake Village, CA called "Copperfield Systems". We develop innovative iPad apps and provide IT consulting services for the Energy industry (specifically Oil and Gas companies).

For consulting services, we provide Business Intelligence solutions to implement Data Warehouse strategies. Our services include Business Intelligence, Data Warehouse, Application Integration and Support. An older consulting brochure we have used in the past under a different company name ("Norwell Data Advisory") is attached for additional background and content. We do not want to use the old design at all - its really just for reference only.

Our first product is called "Fieldpoint KRV" - includes iPad apps and web-based tools that support field production data gathering for Oil and Gas companies. It also includes a Decision Support Center (DSC) to help with route management of field operators using mapping technologies.

The final design should be an overview of the company, products and services with contact information.
Updates

We included some sample content for the areas of company overview, products and services for the brochure (added to attachment area - "Sample Content").  If there is too much content for your design, you do not need to use all of the sample.  We are flexible to re-write all areas to fit the design.

Please let us know if you need more information or have any additional questions about the brochure.

Contact information for the brochure below - 

4187 Halberton Ave. Suite 310
Westlake Village, CA. 91488
United States

+1-805-555-0173
info@copperfieldsystems-example.com
http://www.copperfieldsystems-example.com 

Please Note: Our website above is currently a placeholder, feel free to reference our previous site for additional details -  http://www.norwelldata-example.com

Target Market(s)

Oil and Gas company managers, males between 40 - 55 years old in corporate sector, college education, technical backgrounds

Industry/Entity Type

Industry

Requirements
Must have
• The bi-fold brochure must have 4 pages. It should measure 11" x 17" - folding to 8 1/2" x 11" for each page.
Nice to have
• We have a starter idea for the logo, but we would love to see other ideas. The starter logo ideas are attached but feel free to change it, thanks!

We would love the brochure to have different areas to highlight the company, products and services in an interesting way or layout. It should accommodate a good balance between photos/images and text but the brochure is an overview only of the products and services.

```html
<!DOCTYPE html>
<html lang="en">
<head>
<meta charset="utf-8">
<title>Copperfield Systems – Back Cover</title>
<link rel="stylesheet" href="https://fonts.googleapis.com/css2?family=Open+Sans:wght@400;600;700&family=PT+Sans:wght@400;700&display=swap">
<style>
  :root {
    --navy: #1b2a8c;
    --royal: #1f3fc4;
    --deep-band: #1c2fa3;
    --sky: #2a8ae8;
    --aqua: #7ff2ec;
    --aqua-soft: #b8f7f4;
    --ink: #3a3f48;
    --rule: #9aa3ad;
    --paper: #ffffff;
  }
  * { margin: 0; padding: 0; box-sizing: border-box; }
  html, body { width: 1200px; height: 797px; overflow: hidden; background: var(--paper); }
  .cover {
    position: relative;
    width: 1200px;
    height: 797px;
    overflow: hidden;
    font-family: "PT Sans", sans-serif;
  }
  .cover__backdrop { position: absolute; inset: 0; }
  .headline {
    position: absolute; left: 28px; top: 48px;
    font-family: "Open Sans", sans-serif; font-weight: 700;
    font-size: 24px; color: var(--navy); letter-spacing: 0.2px;
  }
  .contact-panel {
    position: absolute; left: 137px; top: 198px;
    width: 440px; height: 228px;
    background: rgba(255, 255, 255, 0.12);
  }
  .contact-panel__title {
    position: absolute; left: 26px; top: 6px;
    font-family: "Open Sans", sans-serif; font-weight: 700;
    font-size: 20px; color: var(--navy); white-space: nowrap;
  }
  .contact-panel__details {
    position: absolute; left: 26px; top: 64px;
    font-weight: 700; font-size: 17.5px; line-height: 17px;
    color: var(--navy); letter-spacing: -0.3px; white-space: nowrap;
  }
  .contact-panel__details p + p { margin-top: 20px; }
  .contact-panel__details .line-gap { margin-top: 16px; }
  .brand-disc {
    position: absolute; left: 655px; top: 120px;
    width: 230px; height: 230px; border-radius: 50%;
    background: radial-gradient(circle at 40% 40%, rgba(255,255,255,0.55), rgba(120,220,245,0.35));
  }
  .brand-name {
    position: absolute; left: 912px; top: 150px;
    font-family: "Open Sans", sans-serif; font-weight: 400;
    font-size: 43px; line-height: 54px; color: var(--royal);
  }
  .tagline {
    position: absolute; left: 936px; top: 298px;
    padding-left: 14px; border-left: 1.5px solid var(--ink);
    font-family: "Open Sans", sans-serif; font-size: 20px; line-height: 28px;
    color: var(--ink);
  }
  .footer-rule {
    position: absolute; left: 280px; top: 697px; width: 920px; height: 1px;
    background: var(--rule);
  }
  .web-invite {
    position: absolute; left: 405px; top: 711px;
    font-family: "Open Sans", sans-serif; font-size: 19px; color: #2fc3e6;
  }
  .web-address {
    position: absolute; left: 248px; top: 735px;
    font-family: Arial, "Helvetica Neue", sans-serif; font-weight: 700;
    font-size: 16px; color: var(--navy);
  }
  .footer-slash {
    position: absolute; left: 820px; top: 700px; width: 1px; height: 34px;
    background: var(--ink); transform: rotate(30deg); transform-origin: top left;
  }
  .footer-note {
    position: absolute; left: 842px; top: 716px;
    font-family: Arial, sans-serif; font-size: 9.5px; color: #59c6e6; letter-spacing: 0.3px;
  }
  .footer-note strong { color: #2a9ad8; font-weight: 700; }
</style>
</head>
<body>
<main class="cover">
  <svg class="cover__backdrop" width="1200" height="797" viewBox="0 0 1200 797" aria-hidden="true">
    <defs>
      <linearGradient id="sea" x1="0" y1="1" x2="1" y2="0">
        <stop offset="0" stop-color="#1560d8"/>
        <stop offset="0.45" stop-color="#2a95ec"/>
        <stop offset="0.75" stop-color="#63d9f0"/>
        <stop offset="1" stop-color="#8ff5ea"/>
      </linearGradient>
      <linearGradient id="shade" x1="0" y1="0" x2="1" y2="0">
        <stop offset="0" stop-color="#0f2a9a"/>
        <stop offset="1" stop-color="#2450d0"/>
      </linearGradient>
    </defs>
    <rect width="1200" height="797" fill="url(#sea)"/>
    <!-- top-left white field -->
    <path d="M0 0 H640 C520 60 300 130 0 150 Z" fill="#ffffff"/>
    <path d="M0 150 C300 130 520 60 640 0 L700 0 C560 80 330 170 0 200 Z" fill="url(#shade)"/>
    <path d="M0 200 C330 170 560 80 700 0 L720 0 C580 95 340 195 0 232 Z" fill="#ffffff"/>
    <path d="M0 232 C340 195 580 95 720 0 L760 0 C600 110 350 215 0 250 Z" fill="var(--aqua)"/>
    <!-- lower sweep bands -->
    <path d="M0 797 V620 C400 560 800 500 1200 440 V797 Z" fill="#ffffff" opacity="0.35"/>
    <path d="M120 797 C420 600 800 470 1200 430 V470 C820 510 480 630 230 797 Z" fill="#ffffff"/>
    <path d="M230 797 C480 630 820 510 1200 470 V520 C840 560 560 660 380 797 Z" fill="var(--deep-band)"/>
    <path d="M380 797 C560 660 840 560 1200 520 V550 C860 590 620 680 470 797 Z" fill="#ffffff"/>
    <path d="M470 797 C620 680 860 590 1200 550 V600 C900 630 700 700 600 797 Z" fill="var(--aqua)"/>
    <path d="M600 797 C700 700 900 630 1200 600 V640 C960 660 800 720 730 797 Z" fill="var(--royal)"/>
    <path d="M0 797 V690 C400 690 900 650 1200 640 V797 Z" fill="#ffffff"/>
  </svg>

  <h2 class="headline">Put our services to the test</h2>

  <section class="contact-panel">
    <h3 class="contact-panel__title">Contact us for a consultation today</h3>
    <div class="contact-panel__details">
      <p>Copperfield Systems<br>4187 Halberton Ave. Suite 310<br>Westlake Village, CA. 91488<br>United States</p>
      <p>Phone: +1-805-555-0173</p>
      <p>Email: info@copperfieldsystems-example.com</p>
    </div>
  </section>

  <div class="brand-disc" aria-hidden="true"></div>
  <h1 class="brand-name">Copperfield<br>Systems</h1>
  <p class="tagline">Creative Solutions<br>For Oil And Gas</p>

  <div class="footer-rule"></div>
  <p class="web-invite">Visit our Web Page</p>
  <p class="web-address">http://www.copperfieldsystems-example.com</p>
  <div class="footer-slash"></div>
  <p class="footer-note">Information Management Systems: <strong>Innovative Products and Services</strong></p>
</main>
</body>
</html>
```